7Brink Plumbing flyer

I want to incorporate our logo design into a new flyer promoting the business and advertising products that we install.
We install hot water systems, Air-conditioning systems and central heating systems. Along with other aspects of plumbing such as gasfitting, roofing, sanitary and drainage
I would like the background to be the same as our business cards with the water effect and colours.

Requirements
Must have
• Logo
24/7 Emergency call out
Aspects of plumbing we do
- Hot water systems
- Central Heating
- Solar hot water systems/ heat pump systems
- Gasfitting
- Drainage
- Roofing
- Air-Conditioning
Nice to have
• Pictures of hot water systems and air-conditioning system
$30 off voucher when producing this flyer (limit 1 per house hold)

```html
<!DOCTYPE html>
<html lang="en">
<head>
<meta charset="utf-8">
<title>7Brink Plumbing flyer</title>
<link href="https://fonts.googleapis.com/css2?family=Roboto+Condensed:wght@400;700&display=swap" rel="stylesheet">
<style>
  :root{
    --stage:#d9d9db;
    --night:#2a2a2c;
    --night-deep:#1f1f21;
    --blue:#1e8fe0;
    --blue-deep:#1565c0;
    --blue-light:#a9d9f6;
    --white:#ffffff;
  }
  html,body{margin:0;padding:0;width:1200px;height:1200px;overflow:hidden;background:var(--stage);font-family:"Roboto Condensed",Arial,sans-serif;}
  .flyer{position:absolute;top:225px;width:530px;height:752px;overflow:hidden;
    background:radial-gradient(circle at 50% 40%,#343437 0%,var(--night) 55%,var(--night-deep) 100%);}
  .flyer--front{left:60px;}
  .flyer--back{left:610px;}
  .flyer svg.shapes{position:absolute;left:0;top:0;}

  .brand{position:absolute;top:48px;left:0;width:100%;display:flex;justify-content:center;align-items:center;gap:14px;}
  .brand__dot{width:46px;height:46px;border-radius:50%;background:var(--blue);}
  .brand__name{color:#2aa4f0;font-weight:700;font-size:46px;letter-spacing:1px;text-transform:uppercase;line-height:1;}

  .services{position:absolute;left:42px;top:226px;color:var(--white);}
  .services__title{margin:0 0 22px;font-size:30px;line-height:1.05;font-weight:400;letter-spacing:.5px;}
  .services__title strong{display:block;font-weight:700;}
  .services__list{list-style:none;margin:0;padding:0;font-size:19px;}
  .services__list li{position:relative;padding-left:20px;margin-bottom:10px;line-height:1.2;}
  .services__list li::before{content:"";position:absolute;left:0;top:5px;width:11px;height:11px;border-radius:50%;background:var(--blue-light);}

  .voucher{position:absolute;top:26px;left:0;width:100%;height:104px;background:linear-gradient(90deg,var(--blue-deep),var(--blue));color:var(--white);text-align:center;}
  .voucher__line{margin:0;font-weight:700;font-size:26px;line-height:1.28;}
  .voucher__line:first-child{padding-top:10px;}
  .voucher__note{margin:0;font-size:18px;}

  .contact{position:absolute;left:0;width:100%;color:var(--white);font-size:18px;text-align:center;}
  .contact--lic{top:592px;font-size:16px;}
  .contact--row{top:624px;display:flex;justify-content:center;gap:30px;}
  .contact--addr{top:658px;display:flex;justify-content:center;}
  .contact span{display:inline-flex;align-items:center;gap:8px;}
  .contact svg{width:17px;height:17px;fill:#3aa7f0;}

  .web{position:absolute;left:0;top:698px;width:100%;height:32px;background:linear-gradient(90deg,var(--blue-deep),var(--blue));color:var(--white);text-align:center;line-height:32px;font-size:16px;letter-spacing:5px;}
</style>
</head>
<body>

<section class="flyer flyer--front">
  <svg class="shapes" width="530" height="752" viewBox="0 0 530 752">
    <defs>
      <linearGradient id="panelBlue" x1="0" y1="0" x2="1" y2="1">
        <stop offset="0" stop-color="#2aa0ee"/>
        <stop offset="1" stop-color="#1677d2"/>
      </linearGradient>
      <linearGradient id="heaterTone" x1="0" y1="0" x2="1" y2="0">
        <stop offset="0" stop-color="#8a8fb0"/>
        <stop offset=".5" stop-color="#c9ccd6"/>
        <stop offset="1" stop-color="#9da2bd"/>
      </linearGradient>
      <linearGradient id="acTone" x1="0" y1="0" x2="0" y2="1">
        <stop offset="0" stop-color="#4f7ec2"/>
        <stop offset=".6" stop-color="#d9dcd4"/>
        <stop offset="1" stop-color="#4f9a3a"/>
      </linearGradient>
      <path id="badgeTop" d="M 56 656 A 50 50 0 0 1 156 656"/>
      <path id="badgeBottom" d="M 50 668 A 56 56 0 0 0 162 668"/>
    </defs>
    <circle class="services-panel" cx="142" cy="408" r="240" fill="url(#panelBlue)" stroke="#9fd3f5" stroke-width="6"/>
    <g role="img" aria-label="Photo of a stainless steel electric hot water storage tank">
      <circle cx="438" cy="296" r="140" fill="url(#heaterTone)" stroke="#cfe9fb" stroke-width="6"/>
    </g>
    <g role="img" aria-label="Photo of an outdoor air-conditioning unit beside a blue wall and grass">
      <circle cx="310" cy="540" r="112" fill="url(#acTone)" stroke="#cfe9fb" stroke-width="6"/>
    </g>
    <g class="badge">
      <circle cx="106" cy="656" r="64" fill="#1e7fd6" stroke="#ffffff" stroke-width="4"/>
      <circle cx="106" cy="656" r="40" fill="#e8f4fd"/>
      <text font-family="Roboto Condensed, sans-serif" font-weight="700" font-size="12" fill="#ffffff" letter-spacing="1">
        <textPath href="#badgeTop" startOffset="50%" text-anchor="middle">EMERGENCY CALL OUT</textPath>
      </text>
      <text font-family="Roboto Condensed, sans-serif" font-weight="700" font-size="12" fill="#ffffff" letter-spacing="1">
        <textPath href="#badgeBottom" startOffset="50%" text-anchor="middle" dominant-baseline="hanging">EMERGENCY CALL OUT</textPath>
      </text>
      <text x="106" y="666" text-anchor="middle" font-family="Roboto Condensed, sans-serif" font-weight="700" font-size="30" fill="#1a3f8f">24/7</text>
    </g>
  </svg>

  <div class="brand">
    <span class="brand__dot"></span>
    <span class="brand__name">7Brink Plumbing</span>
  </div>

  <div class="services">
    <h2 class="services__title">ASPECTS OF <strong>PLUMBING WE DO:</strong></h2>
    <ul class="services__list">
      <li>Hot water systems</li>
      <li>Central Heating</li>
      <li>Solar hot water systems/<br>heat pump systems</li>
      <li>Gasfitting</li>
      <li>Drainage</li>
      <li>Roofing</li>
      <li>Air-Conditioning</li>
    </ul>
  </div>
</section>

<section class="flyer flyer--back">
  <div class="voucher">
    <p class="voucher__line">$30 off voucher</p>
    <p class="voucher__line">when producing this flyer</p>
    <p class="voucher__note">(limit 1 per house hold)</p>
  </div>

  <svg class="shapes" width="530" height="752" viewBox="0 0 530 752">
    <defs>
      <radialGradient id="plumberTone" cx="50%" cy="45%" r="55%">
        <stop offset="0" stop-color="#2b4f8e"/>
        <stop offset=".7" stop-color="#1d3567"/>
        <stop offset="1" stop-color="#3a9be6"/>
      </radialGradient>
    </defs>
    <g role="img" aria-label="Photo of a smiling plumber in a navy uniform holding a pipe wrench beside a tool bag">
      <circle cx="266" cy="365" r="188" fill="url(#plumberTone)"/>
    </g>
  </svg>

  <p class="contact contact--lic">Lic #: 208417</p>
  <div class="contact contact--row">
    <span><svg viewBox="0 0 24 24"><path d="M6.6 10.8a15.1 15.1 0 0 0 6.6 6.6l2.2-2.2a1 1 0 0 1 1-.25 11.4 11.4 0 0 0 3.6.57 1 1 0 0 1 1 1V20a1 1 0 0 1-1 1A17 17 0 0 1 3 4a1 1 0 0 1 1-1h3.5a1 1 0 0 1 1 1c0 1.25.2 2.45.57 3.57a1 1 0 0 1-.25 1z"/></svg>+61 400 555 217</span>
    <span><svg viewBox="0 0 24 24"><path d="M2 5h20v14H2z M2 5l10 8 10-8" fill="none" stroke="#3aa7f0" stroke-width="0"/><path d="M2 6.5l10 7 10-7V19H2z M3 5h18l-9 6.3z"/></svg>mia@7brinkplumbing.com</span>
  </div>
  <div class="contact contact--addr">
    <span><svg viewBox="0 0 24 24"><path d="M12 2a7 7 0 0 0-7 7c0 5.2 7 13 7 13s7-7.8 7-13a7 7 0 0 0-7-7zm0 9.5A2.5 2.5 0 1 1 12 6.5a2.5 2.5 0 0 1 0 5z"/></svg>P.O Box 902 Fernvale, VIC, Australia 3999</span>
  </div>
  <div class="web">www.7brinkplumbing.com</div>
</section>

</body>
</html>
```